Dog Food Bag Packaging Redesign

Hey there..We're a small dog food company, focusing on all natural, locally sourced, high quality ingredients. They're patties, and baked for 10 min. Dogs go insane for them. We're looking to redo our packaging, and thus, its design. I've attached images. Currently, we are wrapping 12 patties in a poly bag and then butcher paper, and sticking a label on it. We're moving to a zipper seal poly that's black. I've attached the design concept from our bag manufacturer for your reference only. We don't necessarily want to use our old label, but we're not against using elements of it. We really like our current label.. I'm just not so sure it's the right call for a poly bag.We have three flavours; chicken, beef, lamb. I would LOVE to know what flavour the bag is without having to be super close to the bag. So perhaps the top part (1-4 inches) could be the flavour colour? I will have to provide some verbiage for the back. I need to add feeding instructions, and a bit of a thank you story. I'm open for suggestions on how to display ingredients/nutritional facts.

Target Market(s)

Dog Owners

Industry/Entity Type

Manufacturing

Font styles to use
Sans Serif

Colors
9bcb3c

Requirements
Must have
• Total bag design. When you submit your design, please submit your designs on top of a bag. It makes it much easier to visual the end product.
• The bag needs to have the associated flavour colours on it to differentiate flavour from a distance. Red = beef, yellow = chicken, purple = lamb.
• I'm happy with the logo being on the back only, but if on the front it needs to be small. Patties should be the main header word.
Nice to have
• I like the idea of a vertical colour bar on the side of the bag to show its flavour, but I'm not again a top horizontal bar either.
• I like PATTIES being the biggest word on the bag.

```html
<!DOCTYPE html>
<html lang="en">
<head>
<meta charset="utf-8">
<title>Patties Packaging — Beef, Chicken, Lamb</title>
<link rel="stylesheet" href="https://fonts.googleapis.com/css2?family=Bebas+Neue&family=Oswald:wght@400;500;600&display=swap">
<style>
  :root {
    --stage: #dcdcdc;
    --bag: #1d1d1d;
    --bag-seam: #2a2a2a;
    --label: #f7f7f5;
    --footer: #8b2a20;
    --footer-text: #f3e6d8;
    --ingredient-text: #3a2a24;
    --photo-dark: #6e6e6e;
    --photo-light: #cfcfcf;
    --patty-dark: #9c6a2c;
    --patty-light: #d8a458;
  }
  * { margin: 0; padding: 0; box-sizing: border-box; }
  html, body { width: 1200px; height: 632px; overflow: hidden; }
  body {
    background: radial-gradient(ellipse at 50% 40%, #ececec 0%, var(--stage) 70%);
    position: relative;
  }
  .bag {
    position: absolute;
    top: 50px;
    width: 326px;
    height: 535px;
    background: var(--bag);
    border-radius: 4px;
  }
  .bag::before {
    content: "";
    position: absolute;
    left: 12px; right: 12px; top: 70px;
    height: 3px;
    background: var(--bag-seam);
  }
  .bag--beef { left: 79px; }
  .bag--chicken { left: 437px; }
  .bag--lamb { left: 798px; }

  .bag--beef {
    --ink: #a8382a; --band: #e59a2b; --band-text: #1a1a1a;
    --ribbon-top: #9b3225; --ribbon-bottom: #e59a2b; --ribbon-sub: #7a2a1e;
    --accent: #e59a2b;
  }
  .bag--chicken {
    --ink: #f2c624; --band: #eea224; --band-text: #f7de3c;
    --ribbon-top: #eea224; --ribbon-bottom: #f6cf2a; --ribbon-sub: #fff3b0;
    --accent: #f2c624;
  }
  .bag--lamb {
    --ink: #7d5aa6; --band: #7d5aa6; --band-text: #f2d636;
    --ribbon-top: #6b4a95; --ribbon-bottom: #8a67b3; --ribbon-sub: #f2d636;
    --accent: #f2d636;
  }

  .label {
    position: absolute;
    left: 22px; top: 107px;
    width: 282px; height: 401px;
    display: block;
  }
  .label__paper { fill: var(--label); }
  .headline { font-family: "Bebas Neue", sans-serif; fill: var(--ink); }
  .subtitle { font-family: "Oswald", sans-serif; font-weight: 500; fill: var(--ink); }
  .ribbon__top { fill: var(--ribbon-top); }
  .ribbon__bottom { fill: var(--ribbon-bottom); }
  .ribbon__weight { font-family: "Bebas Neue", sans-serif; fill: #fff8e6; }
  .ribbon__count { font-family: "Oswald", sans-serif; font-weight: 500; fill: var(--ribbon-sub); }
  .brand__mark { fill: none; stroke: #5a3a22; stroke-width: 2; }
  .brand__name { font-family: "Oswald", sans-serif; font-weight: 500; fill: #4a3426; }
  .flavour-band { fill: var(--band); }
  .flavour-name { font-family: "Bebas Neue", sans-serif; fill: var(--band-text); }
  .flavour-stars { font-family: "Oswald", sans-serif; fill: var(--band-text); }
  .flavour-icon { fill: var(--band-text); }
  .ingredient { font-family: "Oswald", sans-serif; font-weight: 500; fill: var(--ingredient-text); }
  .ingredient__bullet { fill: var(--footer); }
  .ingredient__rule { stroke: var(--band); stroke-width: 0.6; }
  .footer { fill: var(--footer); }
  .footer__url { font-family: "Bebas Neue", sans-serif; fill: var(--footer-text); }
  .footer__small { font-family: "Oswald", sans-serif; font-weight: 500; fill: var(--footer-text); }
  .footer__dot { fill: var(--accent); }
  .footer__icon { fill: none; stroke: var(--footer-text); stroke-width: 1; }
</style>
</head>
<body>

<!-- Beef -->
<div class="bag bag--beef">
  <svg class="label" viewBox="0 0 282 401" aria-label="Beef patties label">
    <defs>
      <linearGradient id="dog-beef" x1="0" y1="0" x2="1" y2="1"><stop offset="0" stop-color="var(--photo-light)"/><stop offset="1" stop-color="var(--photo-dark)"/></linearGradient>
      <radialGradient id="patty-beef"><stop offset="0" stop-color="var(--patty-light)"/><stop offset="1" stop-color="var(--patty-dark)"/></radialGradient>
    </defs>
    <rect class="label__paper" width="282" height="401"/>
    <rect x="166" y="110" width="116" height="255" fill="url(#dog-beef)" role="img" aria-label="Black and white photo of a hound dog looking up"/>
    <path class="ribbon__bottom" d="M204,22 H241 V56 L222.5,48 L204,56 Z"/>
    <rect class="ribbon__top" x="204" y="0" width="37" height="22"/>
    <text class="ribbon__weight" x="222.5" y="18" font-size="17" text-anchor="middle">3 LB</text>
    <text class="ribbon__count" x="222.5" y="36" font-size="5.5" text-anchor="middle">12 PATTIES</text>
    <circle class="brand__mark" cx="222" cy="76" r="12"/>
    <text class="brand__name" x="222" y="106" font-size="15" text-anchor="middle" letter-spacing="1">PASTURA</text>
    <text class="subtitle" transform="translate(33,230) rotate(-90)" font-size="11" textLength="171" lengthAdjust="spacing">GRASS-FED BEEF</text>
    <text class="headline" transform="translate(108,230) rotate(-90)" font-size="92" textLength="171" lengthAdjust="spacingAndGlyphs">PATTIES</text>
    <rect class="flavour-band" x="0" y="246" width="213" height="40"/>
    <text class="flavour-name" x="16" y="280" font-size="36" letter-spacing="5">BEEF</text>
    <text class="flavour-stars" x="106" y="270" font-size="6" letter-spacing="0.5">★★★★★</text>
    <rect class="flavour-icon" x="140" y="258" width="30" height="16" rx="3" role="img" aria-label="Cow silhouette icon"/>
    <g class="ingredients">
      <circle class="ingredient__bullet" cx="22" cy="301" r="2.5"/><text class="ingredient" x="32" y="304" font-size="6.5" letter-spacing="0.6">GRASS FED BEEF</text><line class="ingredient__rule" x1="20" y1="307" x2="100" y2="307"/>
      <circle class="ingredient__bullet" cx="22" cy="313" r="2.5"/><text class="ingredient" x="32" y="316" font-size="6.5" letter-spacing="0.6">FRESH EGGS</text><line class="ingredient__rule" x1="20" y1="319" x2="100" y2="319"/>
      <circle class="ingredient__bullet" cx="22" cy="325" r="2.5"/><text class="ingredient" x="32" y="328" font-size="6.5" letter-spacing="0.6">APPLE, SWEET POTATOS</text><line class="ingredient__rule" x1="20" y1="331" x2="104" y2="331"/>
      <circle class="ingredient__bullet" cx="22" cy="336" r="2.5"/><text class="ingredient" x="32" y="339" font-size="6.5" letter-spacing="0.6">BROCOLI</text><line class="ingredient__rule" x1="20" y1="342" x2="100" y2="342"/>
      <circle class="ingredient__bullet" cx="22" cy="348" r="2.5"/><text class="ingredient" x="32" y="351" font-size="6.5" letter-spacing="0.6">CARROTS</text>
    </g>
    <ellipse cx="140" cy="328" rx="28" ry="26" fill="url(#patty-beef)" role="img" aria-label="Photo of a stack of baked patties"/>
    <rect class="footer" x="0" y="365" width="282" height="36"/>
    <text class="footer__url" x="16" y="388" font-size="13" letter-spacing="1">GOPASTURA.CA</text>
    <circle class="footer__dot" cx="104" cy="384" r="3"/>
    <rect class="footer__icon" x="113" y="376" width="14" height="15" role="img" aria-label="Local producer badge"/>
    <text class="footer__small" x="132" y="382" font-size="5.5" letter-spacing="0.6">PROUDLY</text>
    <text class="footer__small" x="132" y="390" font-size="5.5" letter-spacing="0.6">MILLBROOK</text>
    <circle class="footer__dot" cx="182" cy="384" r="3"/>
    <circle class="footer__icon" cx="200" cy="380" r="5"/><text class="footer__small" x="200" y="394" font-size="4" text-anchor="middle">FRESH</text>
    <path class="footer__icon" d="M223,385 C219,380 219,375 223,375 C227,375 227,380 223,385 Z"/><text class="footer__small" x="223" y="394" font-size="4" text-anchor="middle">LOCAL</text>
    <circle class="footer__icon" cx="251" cy="380" r="5"/><text class="footer__small" x="251" y="394" font-size="4" text-anchor="middle">RESPONSIBLE</text>
  </svg>
</div>

<!-- Chicken -->
<div class="bag bag--chicken">
  <svg class="label" viewBox="0 0 282 401" aria-label="Chicken patties label">
    <defs>
      <linearGradient id="dog-chicken" x1="0" y1="0" x2="1" y2="1"><stop offset="0" stop-color="var(--photo-light)"/><stop offset="1" stop-color="var(--photo-dark)"/></linearGradient>
      <radialGradient id="patty-chicken"><stop offset="0" stop-color="var(--patty-light)"/><stop offset="1" stop-color="var(--patty-dark)"/></radialGradient>
    </defs>
    <rect class="label__paper" width="282" height="401"/>
    <rect x="166" y="110" width="116" height="255" fill="url(#dog-chicken)" role="img" aria-label="Black and white photo of a hound dog looking up"/>
    <path class="ribbon__bottom" d="M204,22 H241 V56 L222.5,48 L204,56 Z"/>
    <rect class="ribbon__top" x="204" y="0" width="37" height="22"/>
    <text class="ribbon__weight" x="222.5" y="18" font-size="17" text-anchor="middle">3 LB</text>
    <text class="ribbon__count" x="222.5" y="36" font-size="5.5" text-anchor="middle">12 PATTIES</text>
    <circle class="brand__mark" cx="222" cy="76" r="12"/>
    <text class="brand__name" x="222" y="106" font-size="15" text-anchor="middle" letter-spacing="1">PASTURA</text>
    <text class="subtitle" transform="translate(33,230) rotate(-90)" font-size="11" textLength="171" lengthAdjust="spacing">DEBONED CHICKEN</text>
    <text class="headline" transform="translate(108,230) rotate(-90)" font-size="92" textLength="171" lengthAdjust="spacingAndGlyphs">PATTIES</text>
    <rect class="flavour-band" x="0" y="246" width="213" height="40"/>
    <text class="flavour-name" x="12" y="279" font-size="34" letter-spacing="3">CHICKEN</text>
    <text class="flavour-stars" x="144" y="270" font-size="6" letter-spacing="0.5">★★★★★</text>
    <rect class="flavour-icon" x="180" y="256" width="18" height="20" rx="3" role="img" aria-label="Chicken silhouette icon"/>
    <g class="ingredients">
      <circle class="ingredient__bullet" cx="22" cy="301" r="2.5"/><text class="ingredient" x="32" y="304" font-size="6.5" letter-spacing="0.6">DEBONED CHICKEN</text><line class="ingredient__rule" x1="20" y1="307" x2="100" y2="307"/>
      <circle class="ingredient__bullet" cx="22" cy="313" r="2.5"/><text class="ingredient" x="32" y="316" font-size="6.5" letter-spacing="0.6">FRESH EGGS</text><line class="ingredient__rule" x1="20" y1="319" x2="100" y2="319"/>
      <circle class="ingredient__bullet" cx="22" cy="325" r="2.5"/><text class="ingredient" x="32" y="328" font-size="6.5" letter-spacing="0.6">APPLE, SWEET POTATOS</text><line class="ingredient__rule" x1="20" y1="331" x2="104" y2="331"/>
      <circle class="ingredient__bullet" cx="22" cy="336" r="2.5"/><text class="ingredient" x="32" y="339" font-size="6.5" letter-spacing="0.6">BROCOLI</text><line class="ingredient__rule" x1="20" y1="342" x2="100" y2="342"/>
      <circle class="ingredient__bullet" cx="22" cy="348" r="2.5"/><text class="ingredient" x="32" y="351" font-size="6.5" letter-spacing="0.6">CARROTS</text>
    </g>
    <ellipse cx="140" cy="328" rx="28" ry="26" fill="url(#patty-chicken)" role="img" aria-label="Photo of a stack of baked patties"/>
    <rect class="footer" x="0" y="365" width="282" height="36"/>
    <text class="footer__url" x="16" y="388" font-size="13" letter-spacing="1">GOPASTURA.CA</text>
    <circle class="footer__dot" cx="104" cy="384" r="3"/>
    <rect class="footer__icon" x="113" y="376" width="14" height="15" role="img" aria-label="Local producer badge"/>
    <text class="footer__small" x="132" y="382" font-size="5.5" letter-spacing="0.6">PROUDLY</text>
    <text class="footer__small" x="132" y="390" font-size="5.5" letter-spacing="0.6">MILLBROOK</text>
    <circle class="footer__dot" cx="182" cy="384" r="3"/>
    <circle class="footer__icon" cx="200" cy="380" r="5"/><text class="footer__small" x="200" y="394" font-size="4" text-anchor="middle">FRESH</text>
    <path class="footer__icon" d="M223,385 C219,380 219,375 223,375 C227,375 227,380 223,385 Z"/><text class="footer__small" x="223" y="394" font-size="4" text-anchor="middle">LOCAL</text>
    <circle class="footer__icon" cx="251" cy="380" r="5"/><text class="footer__small" x="251" y="394" font-size="4" text-anchor="middle">RESPONSIBLE</text>
  </svg>
</div>

<!-- Lamb -->
<div class="bag bag--lamb">
  <svg class="label" viewBox="0 0 282 401" aria-label="Lamb patties label">
    <defs>
      <linearGradient id="dog-lamb" x1="0" y1="0" x2="1" y2="1"><stop offset="0" stop-color="var(--photo-light)"/><stop offset="1" stop-color="var(--photo-dark)"/></linearGradient>
      <radialGradient id="patty-lamb"><stop offset="0" stop-color="var(--patty-light)"/><stop offset="1" stop-color="var(--patty-dark)"/></radialGradient>
    </defs>
    <rect class="label__paper" width="282" height="401"/>
    <rect x="166" y="110" width="116" height="255" fill="url(#dog-lamb)" role="img" aria-label="Black and white photo of a hound dog looking up"/>
    <path class="ribbon__bottom" d="M204,22 H241 V56 L222.5,48 L204,56 Z"/>
    <rect class="ribbon__top" x="204" y="0" width="37" height="22"/>
    <text class="ribbon__weight" x="222.5" y="18" font-size="17" text-anchor="middle">3 LB</text>
    <text class="ribbon__count" x="222.5" y="36" font-size="5.5" text-anchor="middle">12 PATTIES</text>
    <circle class="brand__mark" cx="222" cy="76" r="12"/>
    <text class="brand__name" x="222" y="106" font-size="15" text-anchor="middle" letter-spacing="1">PASTURA</text>
    <text class="subtitle" transform="translate(33,230) rotate(-90)" font-size="11" textLength="171" lengthAdjust="spacing">DEBONED LAMB</text>
    <text class="headline" transform="translate(108,230) rotate(-90)" font-size="92" textLength="171" lengthAdjust="spacingAndGlyphs">PATTIES</text>
    <rect class="flavour-band" x="0" y="246" width="213" height="40"/>
    <text class="flavour-name" x="20" y="280" font-size="36" letter-spacing="6">LAMB</text>
    <text class="flavour-stars" x="116" y="270" font-size="6" letter-spacing="0.5">★★★★★</text>
    <rect class="flavour-icon" x="164" y="258" width="26" height="17" rx="4" role="img" aria-label="Lamb silhouette icon"/>
    <g class="ingredients">
      <circle class="ingredient__bullet" cx="22" cy="301" r="2.5"/><text class="ingredient" x="32" y="304" font-size="6.5" letter-spacing="0.6">DEBONED LAMB</text><line class="ingredient__rule" x1="20" y1="307" x2="100" y2="307"/>
      <circle class="ingredient__bullet" cx="22" cy="313" r="2.5"/><text class="ingredient" x="32" y="316" font-size="6.5" letter-spacing="0.6">FRESH EGGS</text><line class="ingredient__rule" x1="20" y1="319" x2="100" y2="319"/>
      <circle class="ingredient__bullet" cx="22" cy="325" r="2.5"/><text class="ingredient" x="32" y="328" font-size="6.5" letter-spacing="0.6">APPLE, SWEET POTATOS</text><line class="ingredient__rule" x1="20" y1="331" x2="104" y2="331"/>
      <circle class="ingredient__bullet" cx="22" cy="336" r="2.5"/><text class="ingredient" x="32" y="339" font-size="6.5" letter-spacing="0.6">BROCOLI</text><line class="ingredient__rule" x1="20" y1="342" x2="100" y2="342"/>
      <circle class="ingredient__bullet" cx="22" cy="348" r="2.5"/><text class="ingredient" x="32" y="351" font-size="6.5" letter-spacing="0.6">CARROTS</text>
    </g>
    <ellipse cx="140" cy="328" rx="28" ry="26" fill="url(#patty-lamb)" role="img" aria-label="Photo of a stack of baked patties"/>
    <rect class="footer" x="0" y="365" width="282" height="36"/>
    <text class="footer__url" x="16" y="388" font-size="13" letter-spacing="1">GOPASTURA.CA</text>
    <circle class="footer__dot" cx="104" cy="384" r="3"/>
    <rect class="footer__icon" x="113" y="376" width="14" height="15" role="img" aria-label="Local producer badge"/>
    <text class="footer__small" x="132" y="382" font-size="5.5" letter-spacing="0.6">PROUDLY</text>
    <text class="footer__small" x="132" y="390" font-size="5.5" letter-spacing="0.6">MILLBROOK</text>
    <circle class="footer__dot" cx="182" cy="384" r="3"/>
    <circle class="footer__icon" cx="200" cy="380" r="5"/><text class="footer__small" x="200" y="394" font-size="4" text-anchor="middle">FRESH</text>
    <path class="footer__icon" d="M223,385 C219,380 219,375 223,375 C227,375 227,380 223,385 Z"/><text class="footer__small" x="223" y="394" font-size="4" text-anchor="middle">LOCAL</text>
    <circle class="footer__icon" cx="251" cy="380" r="5"/><text class="footer__small" x="251" y="394" font-size="4" text-anchor="middle">RESPONSIBLE</text>
  </svg>
</div>

</body>
</html>
```